Exciting New Reseller Brand requires Website to WOW New clients to register.

We are a NEW online business called Trade Our Goods.

The Website is a simple concept, it looks to put Merchants (businesses that want their products resold) in touch with Resellers (people or businesses that want to resell that product).

The website acts as an online market place which looks to get Merchants to sign-up and pay to list their company and product as well as getting Resellers to sign-up to view potential Merchants they can get in touch with in the right industry or area to resell their products for (see attached slide-pack to explain packages)

Any type of Industry or Business can register themselves to get listed on Trade Our Goods to see either get their product/service resold or to look for products / services to reseller.

Trade Our Goods does not take any other monetary part in the business relationships other than to obtain money for the monthly website subscription.

We want a very simple website, so this project is for several pages:

Page 1) A really vibrant, exciting, image based homepage to get people to sign-up / register (see sites that we like in the project brief). Needs to be very clear that there are 2 customers and to sign up to join, build and earn!

Page 2) A page that describes the benefits and packages for Resellers.

Page 3) A page that describes the benefits and packages for Merchants.

Page 4) The Payment process pages, taking the customer through sign-up

Page 5) The Business Listings page, so when people search for a Merchant how this will be displayed.

We would really like an image based site and preferably parallax. We want it bright vibrant and to look like a social media site.

All necessary files / logos enclosed.

We would love to continue to work with the winning designer moving forward.

Many thanks and Good Luck.

Regards

Martin & Owen

Target Market(s)

Merchants, Suppliers, Vendors, Manufacturers, Distributors, Wholesalers, Affiliate programs, Franchisees, Reselers

Industry/Entity Type

Business

Number of Pages Required

5+ page

Requirements
Must have
• We love the following websites:
• 1) Like the top section, i.e. parallax image based: www.brightkitestudio.co.uk
• 2) Like the way the screen is split in 2, could be used to describe the 2 different customers we are after Merchants / Resellers: www.filevault-example.com/guide
• 3) Like the bright colours / full screen video split into 2 below top banner and the generally how simple the site is: www.harbourlinden.com.au
• 4) Love all of this site, simple, bold, Love the colours, the clear message and the infographics: http://www.velorin-example.com/swiftrider/faster

```html
<!DOCTYPE html>
<html lang="en">
<head>
<meta charset="utf-8">
<title>Trade Our Goods – Build Your Own Virtual Sales Team</title>
<link rel="stylesheet" href="https://fonts.googleapis.com/css2?family=Raleway:wght@400;500;600&family=Roboto:wght@400;500;700&display=swap">
<style>
:root{
  --blue:#1a8fd6;
  --blue-deep:#0b78c4;
  --green:#8cc63f;
  --green-deep:#7ab52f;
  --ink:#333;
  --muted:#555;
  --footer:#4fb0e2;
  --bar:#363636;
  --white:#fff;
}
*{margin:0;padding:0;box-sizing:border-box}
html,body{width:1200px;height:2557px;overflow:hidden}
body{position:relative;font-family:'Raleway',sans-serif;color:var(--ink);background:var(--white)}
.abs{position:absolute}

/* header + hero */
.hero{left:0;top:0;width:1200px;height:545px;background:radial-gradient(ellipse at 30% 60%,#fbfbfb 0%,#ececec 70%,#e2e2e2 100%);overflow:hidden}
.hero-art{left:753px;top:162px;width:447px;height:383px;background:linear-gradient(135deg,#dfe9f2 0%,#9cc8e8 30%,#8cc63f 65%,#eef4e6 100%)}
.brand{display:flex;align-items:center;gap:12px;font-family:'Raleway',sans-serif;font-weight:600;color:var(--blue)}
.brand-dot{width:40px;height:40px;border-radius:50%;background:var(--green)}
.site-brand{left:90px;top:48px;font-size:28px}
.nav{left:489px;top:62px;font-family:'Roboto',sans-serif;font-size:13px;color:var(--ink)}
.nav a{color:inherit;text-decoration:none;position:absolute;white-space:nowrap}
.nav a.active{color:var(--blue)}
.login{left:1014px;top:51px;width:97px;height:38px;border-radius:4px;background:var(--green);color:#fff;font-family:'Roboto',sans-serif;font-size:15px;display:flex;align-items:center;justify-content:center;letter-spacing:.5px}
.hero-kicker{left:92px;top:258px;font-size:32px;font-weight:500;letter-spacing:.5px}
.hero-title{left:90px;top:314px;font-size:46px;font-weight:500;letter-spacing:1px}
.hero-tag{left:92px;top:391px;font-size:28px;font-weight:500;color:var(--blue);letter-spacing:1px}
.hero-tag span{color:var(--green)}
.dots{left:102px;top:515px;display:flex;gap:8px}
.dots i{display:block;width:27px;height:3px;background:#333}
.dots i.on{background:var(--blue)}

/* split audiences */
.split{top:545px;width:600px;height:302px;color:#fff;text-align:center;font-family:'Roboto',sans-serif}
.split.merchants{left:0;background:linear-gradient(135deg,#2f9ee0,#1a86cc)}
.split.resellers{left:600px;background:linear-gradient(135deg,#9fcd4a,#84b936)}
.split h2,.split h3,.split p{position:absolute;left:40px;right:-40px}
.split.resellers h2,.split.resellers h3,.split.resellers p{left:20px;right:-20px}
.split h2{top:62px;font-size:31px;font-weight:500;letter-spacing:.5px}
.split h3{top:116px;font-size:21px;font-weight:500}
.split p{top:156px;font-size:15px}
.signup{position:absolute;top:202px;left:261px;width:155px;height:54px;border-radius:6px;background:linear-gradient(#fafafa,#d6d6d6);color:var(--ink);font-size:20px;font-weight:500;display:flex;align-items:center;justify-content:center}
.split.resellers .signup{left:243px}

/* why reselling */
.why-label{left:91px;top:906px;font-size:30px;font-weight:500;color:var(--ink)}
.why-label .b{color:var(--blue)}.why-label .g{color:var(--green)}
.why-sub{left:91px;top:960px;font-size:24px;font-weight:500}
.why-big{left:88px;top:992px;font-size:65px;font-weight:400}
.why-big span{color:var(--green)}
.why-list{left:88px;top:1090px;list-style:none;font-size:21px;color:var(--muted)}
.why-list li{height:39px}
.why-list em{font-style:normal;color:var(--blue)}
.why-art{left:597px;top:875px;width:508px;height:400px;background:linear-gradient(90deg,#1a6fc0 0%,#c4c4c4 50%,#9ccd3a 100%);opacity:.85}

/* benefits */
.benefits{top:1345px;width:600px;height:360px;overflow:hidden;color:#fff}
.benefits.merchants{left:0;background:var(--blue-deep)}
.benefits.resellers{left:600px;background:var(--green)}
.benefits-title{left:0;width:1200px;top:1364px;text-align:center;font-size:33px;font-weight:600;color:#fff}
.benefits h2{position:absolute;left:94px;top:104px;font-size:35px;font-weight:600}
.benefits.resellers h2{left:39px}
.benefits ul{position:absolute;left:94px;top:170px;list-style:none;font-size:19px;font-weight:500}
.benefits.resellers ul{left:39px}
.benefits li{height:34.5px}
.benefits .deco{position:absolute;top:70px;height:290px}
.merchants .deco{left:366px;width:234px;background:linear-gradient(160deg,#18a9f0 0%,#5cc2f2 45%,#e8f4fb 100%)}
.resellers .deco{left:377px;width:223px;background:linear-gradient(200deg,#f4fbe9 0%,#d9ec9a 40%,#f5f52a 100%)}

/* portal */
.portal-brand{left:0;width:1200px;top:1768px;justify-content:center;font-size:36px}
.portal-brand .brand-dot{width:50px;height:50px}
.monitor{left:150px;top:1832px;width:370px;height:358px;background:linear-gradient(160deg,#1c2a6b 0%,#2a64c8 45%,#d9d9d9 75%,#bdbdbd 100%)}
.portal-list{left:610px;top:1882px;list-style:none;font-size:21px;color:var(--muted)}
.portal-list li{height:47.5px}
.portal-list .g{color:var(--green)}.portal-list .b{color:var(--blue)}

/* footer */
.footer{left:0;top:2253px;width:1200px;height:213px;background:var(--footer);color:#fff;font-family:'Roboto',sans-serif}
.fcol{position:absolute;top:44px}
.fcol h4{font-size:13px;font-weight:400;letter-spacing:.5px;margin-bottom:17px}
.fcol ul{list-style:none;font-size:12px;line-height:21px}
.testi{font-size:10.5px;line-height:17px;font-style:italic;width:210px}
.testi small{display:block;font-style:normal;margin-top:6px;font-size:10.5px}
.news p{font-size:10.5px;line-height:16px;width:210px}
.email{margin-top:6px;width:208px;height:30px;background:#fff;color:#555;font-size:11px;padding:8px 10px}
.subscribe{margin-top:10px;width:82px;height:25px;background:linear-gradient(#f4f4f4,#cfcfcf);color:#444;font-size:10px;display:flex;align-items:center;justify-content:center;border-radius:2px}
.fcol ul.social{margin-top:-10px}
.social li{display:flex;align-items:center;gap:14px;height:41px;font-size:12px}
.social i{display:block;width:26px;height:26px;border-radius:50%;background:#fff;border:3px solid #2d5da8}
.copyright{left:0;top:2466px;width:1200px;height:91px;background:var(--bar);color:#fff;font-family:'Roboto',sans-serif;font-size:12px;text-align:center;padding-top:40px}
</style>
</head>
<body>

<section class="abs hero">
  <div class="abs hero-art" role="img" aria-label="Decorative graphic in green, blue and white sweeping shapes"></div>
</section>

<div class="abs brand site-brand"><span class="brand-dot"></span>Trade Our Goods</div>
<nav class="abs nav">
  <a class="active" style="left:0">HOME</a>
  <a style="left:72px">MERCHANTS</a>
  <a style="left:181px">RESELLER</a>
  <a style="left:277px">SERVICES</a>
  <a style="left:370px">BLOG</a>
  <a style="left:438px">CONTACTS</a>
</nav>
<div class="abs login">LOGIN</div>

<p class="abs hero-kicker">BUILDING YOUR OWN</p>
<h1 class="abs hero-title">VIRTUAL SALES TEAM</h1>
<p class="abs hero-tag">JOIN . <span>BUILD</span> . EARN</p>
<div class="abs dots"><i class="on"></i><i></i><i></i><i></i><i></i></div>

<section class="abs split merchants" role="img" aria-label="Blue-tinted photo of business people in a meeting">
  <h2>MERCHANTS</h2>
  <h3>GROW BUSINESS &amp; INCREASE SALES</h3>
  <p>Lorem Ipsum is simply dummy text of the printing and typesetting industry</p>
  <div class="signup">SIGN UP</div>
</section>
<section class="abs split resellers" role="img" aria-label="Green-tinted photo of a team working at a table">
  <h2>RESELLERS</h2>
  <h3>GROW PORTFOLIO &amp; INCREASE INCOME</h3>
  <p>Lorem Ipsum is simply dummy text of the printing and typesetting industry</p>
  <div class="signup">SIGN UP</div>
</section>

<h2 class="abs why-label"><span class="b">WHY</span> PICKRE <span class="g">SELLING</span></h2>
<p class="abs why-sub">Bringing reseller opportunities</p>
<p class="abs why-big">to the <span>masses..</span></p>
<ul class="abs why-list">
  <li>• <em>Personal requirement</em> for a reseller base.</li>
  <li>• Experienced <em>reseller models that work.</em></li>
  <li>• Building an <em>effective virtual sales team.</em></li>
  <li>• Helping SME's <em>earn money for old rope.</em></li>
  <li>• Easy to <em>generate revenue</em> for a <em>minimal cost.</em></li>
</ul>
<div class="abs why-art" role="img" aria-label="Illustration of two business silhouettes shaking hands in blue and green before a grey crowd"></div>

<section class="abs benefits merchants">
  <div class="deco" role="img" aria-label="Decorative graphic in light blue and white"></div>
  <h2>MERCHANTS</h2>
  <ul>
    <li>• Additional Source of Sales</li>
    <li>• Incremental Growth</li>
    <li>• Viral Brand Recognition</li>
    <li>• Virtual Sales Team</li>
    <li>• No Overheads</li>
  </ul>
</section>
<section class="abs benefits resellers">
  <div class="deco" role="img" aria-label="Decorative graphic in yellow and white"></div>
  <h2>RESELLERS</h2>
  <ul>
    <li>• Additional Stream of Income</li>
    <li>• Infrastructure in Place</li>
    <li>• No Additional Cost</li>
    <li>• Expand Product Suite</li>
    <li>• Reach New Target Markets</li>
  </ul>
</section>
<h2 class="abs benefits-title">Benefitsforeveryone</h2>

<div class="abs brand portal-brand"><span class="brand-dot"></span>Trade Our Goods</div>
<div class="abs monitor" role="img" aria-label="Desktop monitor showing the website homepage"></div>
<ul class="abs portal-list">
  <li>• Portal for <span class="g">Resellers</span> and <span class="b">Merchants.</span></li>
  <li>• Merchants can <span class="b">promote their products.</span></li>
  <li>• Merchants can <span class="b">build a virtual sales team.</span></li>
  <li>• Resellers can <span class="g">expand product portfolio.</span></li>
  <li>• Resellers can <span class="g">generate revenue.</span></li>
  <li>• <span class="g">Industry news</span> and <span class="b">opportunities.</span></li>
</ul>

<footer class="abs footer">
  <div class="fcol" style="left:89px"><h4>QUICK LINKS</h4>
    <ul><li>Home</li><li>Services</li><li>Gallery</li><li>Testimonials</li><li>Contact us</li></ul></div>
  <div class="fcol" style="left:266px"><h4>SUPPORT LINKS</h4>
    <ul><li>Partners</li><li>Gallery</li><li>Contact Us</li><li>Privacy Policy</li><li>Term of Use</li></ul></div>
  <div class="fcol" style="left:448px"><h4>CLIENT'S TESTIMONIALS</h4>
    <p class="testi">“ Lorem Ipsum has been the industry's standard dummy text ever since the 1500s, when an unknown printer took a galley of type and scrambled it to make a type specimen book. It has survived not only five cen-<small>Client name, City</small></p></div>
  <div class="fcol news" style="left:741px"><h4>NEWSLETTERS SIGN UP</h4>
    <p>Sign up for our daily email by entering your information below</p>
    <div class="email">Email address</div>
    <div class="subscribe">SUBSCRIBE</div></div>
  <div class="fcol" style="left:1019px"><h4>FOLLOW US</h4>
    <ul class="social"><li><i></i>Chatterly</li><li><i></i>Chirpline</li><li><i></i>Circlespace</li></ul></div>
</footer>
<div class="abs copyright">Copyright © 2015 All Rights Reserved</div>

</body>
</html>
```